Tallow Creek Biotics - Business Card Design

Business Card Brief;
We require a design for a business card template for our business “Tallow Creek Biotics”.
We are a firm that manufacture positive microbial formulations to enhance agricultural legume crops such as lucence, soy beans and faba beans. We also manufacture microbial formulations that aid in composting of waste organic waste to use as a natural fertilizer.
We are seeking a business card design that portrays a clean, professional organisation dedicated to enhancing nature and sustainable farming techniques.
Our website is www.soilvantage.com.au
Here is a link to a drawing of a soybean plant. One of our main products is used to help grow these. I offer it an an example of the type of graphic that might be used on the card, but will leave you to create your own design; https://pixelvaultimages.com/482915066/stock-illustration-soybean-plant-on-a-white.html
Two cards are required;
--------------------------------------------------------------------
Card #1
Cody R Whitfield
Executive Chairman
Mobile: 0471 583204
Email: cody@soilvantage.com.au
---------------------------------------------------------------------------
Card #2
Lachlan P Doyce
Chief Financial & Operating Officer
Mobile: 0456 792418
Email lachlan@soilvantage.com.au

Many thanks
Lachlan Doyce

Industry/Entity Type

Agriculture

Colors

Designer to choose colors to be used in the design.

Requirements
Must have
• An elegant design that demonstrates our commitment to enhancing nature.

```html
<!DOCTYPE html>
<html lang="en">
<head>
<meta charset="utf-8">
<title>Tallow Creek Biotics – Business Card</title>
<link rel="stylesheet" href="https://fonts.googleapis.com/css2?family=Montserrat:wght@400;500&family=Open+Sans:wght@400;700&display=swap">
<style>
  :root {
    --bg: #e4e4e4;
    --ink: #111111;
    --paper: #ffffff;
    --mid-grey: #8c8c8c;
    --dark-grey: #3a3a3a;
    --logo-on-dark: #4a4a4a;
  }
  * { margin: 0; padding: 0; box-sizing: border-box; }
  html, body { width: 1200px; height: 782px; overflow: hidden; }
  body {
    background: var(--bg);
    font-family: "Open Sans", Arial, sans-serif;
    color: var(--ink);
    position: relative;
  }
  .card {
    position: absolute;
    top: 237px;
    width: 540px;
    height: 308px;
    overflow: hidden;
    box-shadow: 0 6px 18px rgba(0,0,0,0.25);
  }
  .card--front { left: 40px; background: var(--paper); }
  .card--back { left: 620px; background: var(--ink); }

  .card__wave { position: absolute; left: 0; top: 0; width: 540px; height: 308px; }

  .holder { position: absolute; left: 30px; top: 28px; }
  .holder__name { font-weight: 700; font-size: 15px; letter-spacing: 0.3px; text-transform: uppercase; }
  .holder__title { font-size: 12px; margin-top: 1px; }

  .contact { position: absolute; left: 30px; top: 102px; list-style: none; font-size: 12px; line-height: 16px; }
  .contact__item { display: flex; align-items: center; gap: 6px; }
  .contact__icon { width: 10px; height: 10px; flex: none; }
  .contact__address { margin-top: 1px; }

  .brand { position: absolute; display: flex; align-items: center; gap: 12px; font-family: "Montserrat", Arial, sans-serif; font-weight: 500; }
  .brand__dot { border-radius: 50%; flex: none; }
  .brand__name { line-height: 1.05; }

  .brand--front { left: 260px; top: 118px; color: var(--ink); }
  .brand--front .brand__dot { width: 46px; height: 46px; background: var(--dark-grey); }
  .brand--front .brand__name { font-size: 28px; }

  .brand--back { left: 150px; top: 124px; color: var(--logo-on-dark); }
  .brand--back .brand__dot { width: 42px; height: 42px; background: var(--logo-on-dark); }
  .brand--back .brand__name { font-size: 25px; }
</style>
</head>
<body>

<section class="card card--front" aria-label="Business card front">
  <svg class="card__wave" viewBox="0 0 540 308" aria-hidden="true">
    <path d="M0,172 C110,232 300,250 540,258 L540,270 C300,262 110,244 0,190 Z" fill="var(--mid-grey)"/>
    <path d="M0,196 C110,250 300,268 540,276 L540,308 L0,308 Z" fill="var(--ink)"/>
  </svg>

  <div class="holder">
    <p class="holder__name">Cody R Whitfield</p>
    <p class="holder__title">Executive Chairman</p>
  </div>

  <ul class="contact">
    <li class="contact__item">
      <svg class="contact__icon" viewBox="0 0 10 10"><path d="M2 0.5 L4 2.5 L3 4 Q4.5 6 6 7 L7.5 6 L9.5 8 L8 9.5 Q3 9 0.5 2 Z" fill="var(--ink)"/></svg>
      0471 583204
    </li>
    <li class="contact__item">
      <svg class="contact__icon" viewBox="0 0 10 10"><rect x="0.5" y="2" width="9" height="6.5" fill="var(--ink)"/><path d="M0.8 2.4 L5 5.6 L9.2 2.4" stroke="var(--paper)" stroke-width="0.9" fill="none"/></svg>
      cody@soilvantage.com.au
    </li>
    <li class="contact__item">
      <svg class="contact__icon" viewBox="0 0 10 10"><circle cx="5" cy="5" r="4.5" fill="var(--ink)"/><path d="M0.8 5 H9.2 M5 0.6 Q2.5 5 5 9.4 M5 0.6 Q7.5 5 5 9.4" stroke="var(--paper)" stroke-width="0.7" fill="none"/></svg>
      www.soilvantage.com.au
    </li>
    <li class="contact__address">27 Wattle Row, Dubbo<br>NSW 2830 Australia</li>
  </ul>

  <div class="brand brand--front">
    <span class="brand__dot"></span>
    <span class="brand__name">Tallow Creek<br>Biotics</span>
  </div>
</section>

<section class="card card--back" aria-label="Business card back">
  <div class="brand brand--back">
    <span class="brand__dot"></span>
    <span class="brand__name">Tallow Creek<br>Biotics</span>
  </div>
</section>

</body>
</html>
```